Business Card Design for Vantor Gear

We want to have a business card design for our company.
Company website: www.vantorgear-example.com.au
We looking for something cool, funky, and impressive, yet elegant.
Below are the contents that should be displayed on the card:
Front:
Name: Mark Dellow
Title: Sales & Purchasing
Company Name: Vantor Gear Pty Ltd
Phone: 02 5550 1473
Mobile: 0400 555 019
Email: mark@vantorgear-example.com.au
Website: www.vantorgear-example.com.au
Address: 17 Brackley St
Harwood Vale, NSW 2199
Back:
We buy sell new used Norvex and network equipment
• Huge Savings - save up to 95% off list prices
• Highest Reliability
• Comprehensive Warranty
• Fast delivery
• Large range of hardware in stock
Our logo can be downloaded at: www.vantorgear-example.com.au/logo.zip

```html
<!DOCTYPE html>
<html lang="en">
<head>
<meta charset="utf-8">
<title>Vantor Gear – Business Card</title>
<link rel="stylesheet" href="https://fonts.googleapis.com/css2?family=Source+Sans+3:wght@400;600;700&display=swap">
<style>
  :root {
    --bg: #e9e6e1;
    --paper: #f7f7f7;
    --blue-deep: #1b3c9e;
    --blue-mid: #1f63c8;
    --blue-bright: #2a9be6;
    --ink: #2e3338;
    --brand: #1d4fa6;
    --accent: #f07a1a;
    --accent-warm: #f6c02c;
    --accent-red: #d9322a;
    --white: #ffffff;
  }
  * { box-sizing: border-box; margin: 0; padding: 0; }
  html, body { width: 1200px; height: 880px; overflow: hidden; }
  body {
    background: var(--bg);
    font-family: "Source Sans 3", "Myriad Pro", sans-serif;
    position: relative;
  }
  .card {
    position: absolute;
    left: 280px;
    width: 640px;
    height: 390px;
    overflow: hidden;
    box-shadow: 0 6px 18px rgba(0,0,0,.18);
  }

  /* ---------- Front ---------- */
  .card-front { top: 30px; background: var(--paper); }
  .front-band { position: absolute; inset: 0; }
  .person {
    position: absolute; right: 34px; top: 58px; text-align: right; color: var(--white);
  }
  .person-name { font-size: 27px; font-weight: 700; line-height: 1.1; }
  .person-title { font-size: 18px; font-weight: 400; margin-top: 2px; }

  .brand { position: absolute; left: 36px; top: 140px; display: flex; align-items: center; gap: 14px; }
  .brand-dot { width: 44px; height: 44px; border-radius: 50%; background: var(--accent); flex: none; }
  .brand-name { font-size: 36px; font-weight: 600; color: var(--brand); line-height: 1; }
  .brand-tagline {
    position: absolute; left: 94px; top: 182px;
    font-size: 10px; letter-spacing: 3px; color: var(--brand); text-transform: uppercase;
  }

  .web-rule {
    position: absolute; left: 36px; top: 262px; width: 270px; height: 2px;
    background: linear-gradient(90deg, transparent, var(--blue-mid) 40%, transparent);
  }
  .website { position: absolute; left: 40px; top: 276px; font-size: 17px; color: var(--ink); letter-spacing: .3px; }

  .contacts { position: absolute; left: 336px; top: 196px; list-style: none; }
  .contacts li { display: flex; align-items: flex-start; gap: 10px; font-size: 17px; color: var(--ink); line-height: 1.2; margin-bottom: 7px; }
  .contacts li.address { margin-top: 12px; }
  .contacts svg { width: 17px; height: 17px; flex: none; margin-top: 1px; fill: var(--blue-mid); }

  /* ---------- Back ---------- */
  .card-back {
    top: 460px;
    background: linear-gradient(100deg, var(--blue-deep) 0%, var(--blue-mid) 45%, var(--blue-bright) 100%);
    color: var(--white);
  }
  .back-title { position: absolute; left: 34px; top: 18px; font-size: 56px; font-weight: 600; line-height: 1; }
  .back-tagline { position: absolute; left: 38px; top: 82px; font-size: 11px; letter-spacing: 5px; text-transform: uppercase; }
  .benefits { position: absolute; left: 38px; top: 140px; list-style: none; font-size: 17px; line-height: 1.35; }
  .benefits li { margin-bottom: 6px; }
  .benefits li::before { content: "• "; }
  .back-feature {
    position: absolute; right: 0; top: 70px; width: 270px; height: 320px;
    border-radius: 140px 0 0 0;
    background: radial-gradient(circle at 45% 40%, var(--accent-warm) 0%, var(--accent) 45%, var(--accent-red) 100%);
    opacity: .92;
  }
</style>
</head>
<body>

<section class="card card-front">
  <svg class="front-band" viewBox="0 0 640 390" preserveAspectRatio="none" aria-hidden="true">
    <defs>
      <linearGradient id="bandFill" x1="0" y1="0" x2="1" y2="1">
        <stop offset="0" stop-color="#2a9be6"/>
        <stop offset="1" stop-color="#1b3c9e"/>
      </linearGradient>
    </defs>
    <path d="M0 0 H640 V210 C520 150 300 80 0 58 Z" fill="url(#bandFill)"/>
    <path d="M120 40 C320 70 480 120 640 180" stroke="#ffffff" stroke-opacity=".25" fill="none"/>
    <path d="M200 30 C360 60 500 110 640 160" stroke="#ffffff" stroke-opacity=".2" fill="none"/>
    <path d="M0 58 C300 80 520 150 640 210" stroke="#1b3c9e" stroke-width="3" fill="none"/>
  </svg>

  <div class="person">
    <p class="person-name">Mark Dellow</p>
    <p class="person-title">Sales &amp; Purchasing</p>
  </div>

  <div class="brand">
    <span class="brand-dot"></span>
    <span class="brand-name">Vantor Gear</span>
  </div>
  <p class="brand-tagline">Networking Equipment</p>

  <div class="web-rule"></div>
  <p class="website">www.vantorgear-example.com.au</p>

  <ul class="contacts">
    <li>
      <svg viewBox="0 0 16 16"><rect x="2" y="1" width="12" height="14" rx="2"/><rect x="4.5" y="3" width="7" height="4" fill="#f7f7f7"/></svg>
      02 5550 1473
    </li>
    <li>
      <svg viewBox="0 0 16 16"><rect x="4" y="1" width="8" height="14" rx="1.5"/><rect x="5.5" y="3" width="5" height="7" fill="#f7f7f7"/></svg>
      0400 555 019
    </li>
    <li>
      <svg viewBox="0 0 16 16"><rect x="1" y="3" width="14" height="10" rx="1"/><path d="M1.5 3.5 L8 9 L14.5 3.5" stroke="#f7f7f7" stroke-width="1.4" fill="none"/></svg>
      mark@vantorgear-example.com.au
    </li>
    <li class="address">
      <svg viewBox="0 0 16 16"><path d="M8 1 L15 8 H13 V15 H9.5 V10.5 H6.5 V15 H3 V8 H1 Z"/></svg>
      <span>17 Brackley St<br>Harwood Vale, NSW 2199</span>
    </li>
  </ul>
</section>

<section class="card card-back">
  <div class="back-feature" role="img" aria-label="Large decorative brand graphic in orange, yellow and red tones"></div>
  <p class="back-title">Vantor Gear</p>
  <p class="back-tagline">Networking Equipment</p>
  <ul class="benefits">
    <li>Huge Savings - save up to<br>&nbsp;&nbsp;95% off list prices</li>
    <li>Highest Reliability</li>
    <li>Comprehensive Warranty</li>
    <li>Fast delivery</li>
    <li>Large range of hardware in stock</li>
  </ul>
</section>

</body>
</html>
```